VALTERRA Constructions stationery

Want following designed. Business cards. Letterhead. Email footer. A4 folder cover - front and side. Postcard. For two logo's. VALTERRA CONSTRUCTIONS and VALTERRA INTERIOR DESIGN. Logo's will be provided. Logo is black and metallic Gold.

We are a high end residential design and build company that builds for ourself and exclusive clients who we select to build for. We don't target high volume but high quality projects and build only for clients who pass a number of checks. Ultimately we choose our client and build very high end finishes in remodelling or new home builds. We have no website but will be designing one in the next month.

Target Market(s)

High end residential homes

Industry/Entity Type

Residential Construction

Font styles to use
Serif

Colors
000000
ffc214

Requirements
Must have
• Clean and simplistic. Must represent high end, sophistication, perfection and be sharp.
Nice to have
• We are a high end design and build company that is exclusive to clients we select to build for. We also add our own eclusive one off designs in each build for bathrooms and kitchens like towel rails, vanitys etc.
Should not have
• Animation or unsophisticated

```html
<!DOCTYPE html>
<html lang="en">
<head>
<meta charset="utf-8">
<title>VALTERRA Interior Design – Folder</title>
<link rel="stylesheet" href="https://fonts.googleapis.com/css2?family=Open+Sans:wght@400;600;700&display=swap">
<style>
  :root{
    --stage:#2f2f2f;
    --cover:#131315;
    --cover-edge:#0a0a0b;
    --gold-dark:#7a5c1a;
    --gold-mid:#a7842c;
    --gold-light:#cdaa42;
    --gold-text:#b08a2a;
    --white:#ffffff;
    --ghost:#3b3b3d;
    --label:#9a9a9a;
    --card-white:#f6f6f4;
  }
  *{margin:0;padding:0;box-sizing:border-box}
  html,body{width:1200px;height:1054px;overflow:hidden;background:var(--stage)}
  body{position:relative;font-family:"Open Sans",Arial,sans-serif}
  .dieline{position:absolute;left:0;top:0}
  .abs{position:absolute}

  .flap-url{
    position:absolute;font-size:10px;letter-spacing:1.6px;color:var(--white);
    transform:rotate(-90deg);transform-origin:center;white-space:nowrap;width:150px;text-align:center;
  }
  .flap-url.left{left:21px;top:260px}
  .flap-url.right{left:1035px;top:260px}

  .brand{position:absolute;text-align:left;font-weight:600;text-transform:uppercase;line-height:1}
  .brand .name{font-size:40px;letter-spacing:2px}
  .brand .sub{font-size:17.5px;letter-spacing:1.5px;margin-top:6px}
  .brand .tagline{font-size:12.5px;font-weight:400;text-transform:none;margin-top:8px;letter-spacing:.1px}
  .brand.main{left:720px;top:373px;color:var(--white)}
  .brand.ghost{left:222px;top:373px;color:var(--ghost)}

  .contacts{position:absolute;left:146px;top:632px;list-style:none;color:var(--white);font-size:10px;line-height:13px}
  .contacts li{display:flex;align-items:center;gap:7px}
  .contacts svg{width:8px;height:8px;fill:var(--gold-light)}

  .card{
    position:absolute;left:754px;top:745px;width:206px;height:117px;border-radius:7px;overflow:hidden;
    transform:rotate(-7deg);box-shadow:0 4px 10px rgba(0,0,0,.35);background:var(--card-white)
  }
  .card-top{height:76px;background:var(--cover);padding:16px 0 0 40px;color:var(--white);font-weight:600;text-transform:uppercase;line-height:1}
  .card-top .name{font-size:19px;letter-spacing:1px}
  .card-top .sub{font-size:9px;letter-spacing:.8px;margin-top:3px}
  .card-top .tagline{font-size:5.5px;font-weight:400;text-transform:none;margin-top:4px}
  .card-person{position:absolute;left:18px;top:85px;line-height:1.15}
  .card-person .who{font-size:7px;font-weight:700;color:var(--gold-text);text-transform:uppercase}
  .card-person .role{font-size:5px;font-weight:700;color:#222}
  .card-person .note{font-size:4.5px;color:#777}
  .card-contact{position:absolute;right:12px;top:82px;font-size:5px;line-height:7px;color:#333;text-align:right;list-style:none}

  .caption{position:absolute;left:0;width:1204px;top:955px;text-align:center;font-size:11px;font-weight:600;color:var(--label)}
</style>
</head>
<body>

<svg class="dieline" width="1200" height="1054" viewBox="0 0 1200 1054" aria-hidden="true">
  <defs>
    <linearGradient id="flapGold" x1="0" y1="0" x2="0" y2="1">
      <stop offset="0" stop-color="#7a5c1a"/>
      <stop offset="0.45" stop-color="#c9a63f"/>
      <stop offset="0.6" stop-color="#c9a63f"/>
      <stop offset="1" stop-color="#7a5c1a"/>
    </linearGradient>
    <radialGradient id="pocketLeft" cx="0.45" cy="0.5" r="0.7">
      <stop offset="0" stop-color="#c9a63f"/>
      <stop offset="1" stop-color="#7a5c1a"/>
    </radialGradient>
    <radialGradient id="pocketRight" cx="0.55" cy="0.5" r="0.7">
      <stop offset="0" stop-color="#c9a63f"/>
      <stop offset="1" stop-color="#7a5c1a"/>
    </radialGradient>
    <linearGradient id="coverShade" x1="0" y1="0" x2="0" y2="1">
      <stop offset="0" stop-color="#161618"/>
      <stop offset="1" stop-color="#111113"/>
    </linearGradient>
  </defs>

  <!-- pockets -->
  <path class="pocket" d="M149,695 L601,695 L570,898 Q565,924 538,924 L149,924 Z" fill="url(#pocketLeft)"/>
  <path class="pocket" d="M604,695 L1055,695 L1055,924 L668,924 Q641,924 636,898 Z" fill="url(#pocketRight)"/>

  <!-- side flaps -->
  <path class="flap" d="M116,82 L76,90 L76,447 A20 20 0 0 1 76,487 L76,685 L116,695 Z" fill="url(#flapGold)"/>
  <path class="flap" d="M1090,82 L1130,90 L1130,447 A20 20 0 0 0 1130,487 L1130,685 L1090,695 Z" fill="url(#flapGold)"/>

  <!-- cover -->
  <rect class="cover" x="116" y="82" width="974" height="613" fill="url(#coverShade)" stroke="var(--cover-edge)" stroke-width="1"/>
</svg>

<div class="flap-url left">valterradesign.com.au</div>
<div class="flap-url right">valterradesign.com.au</div>

<div class="brand ghost">
  <div class="name">VALTERRA</div>
  <div class="sub">Interior Design</div>
  <div class="tagline">Interior Architecture &nbsp;- Space design &nbsp;- Staging</div>
</div>

<div class="brand main">
  <div class="name">VALTERRA</div>
  <div class="sub">Interior Design</div>
  <div class="tagline">Interior Architecture &nbsp;- Space design &nbsp;- Staging</div>
</div>

<ul class="contacts">
  <li><svg viewBox="0 0 10 10"><path d="M2 0.5 L3.8 2.6 L2.8 3.6 Q4 6 6.4 7.2 L7.4 6.2 L9.5 8 L8.3 9.5 Q3 9 0.5 1.7 Z"/></svg>0400 555 218</li>
  <li><svg viewBox="0 0 10 10"><path d="M0 2 H10 V8 H0 Z M0 2 L5 5.5 L10 2" stroke="#131315" stroke-width=".8"/></svg>clara@valterradesign.com.au</li>
  <li><svg viewBox="0 0 10 10"><circle cx="5" cy="5" r="4.6"/></svg>valterradesign.com.au</li>
</ul>

<div class="card">
  <div class="card-top">
    <div class="name">VALTERRA</div>
    <div class="sub">Interior Design</div>
    <div class="tagline">Interior Architecture - Space design - Staging</div>
  </div>
  <div class="card-person">
    <div class="who">Clara Whitfield</div>
    <div class="role">DESIGNER</div>
    <div class="note">Residential Interiors</div>
  </div>
  <ul class="card-contact">
    <li>0400 555 218</li>
    <li>clara@valterradesign.com.au</li>
    <li>valterradesign.com.au</li>
  </ul>
</div>

<div class="caption">Folder</div>

</body>
</html>
```